K9 Orbit needs a business card designed

We need a business card designed for K9 Orbit, an expansion of K9 Systems Pty Ltd (www.k9systems.com.au)

We provide high quality professional services for the Australian space industry. Our clients include the Southern Launch Bureau and companies working in the space industry. We identify people with space related skills both locally and internationally who are then contracted by clients to create products and support space launch activities.

Colours to be used:
- Navy blue #000080
- Rocket metallic #8A7F8D
- Platinum #E5E4E2
- Black #000000
- White #FFFFFF

*Front of the card*
I have attached our K9 Orbit logo, which needs to be the main item on the card. The 'Space' text should be placed to the right of the 'K9' part rather than below, similar to the attached K9 Systems card, which this card should match.

If subtext is included, however, it should read ‘Labour Hire • Consultancy • Project Delivery’ rather than the ‘Design • Build • Test • Maintain’ of the K9 Systems card.

A black background (rather than blue background in the K9 Systems card) might be good, with a white pattern as in the K9 Systems card. If colour is used, the logo should be in its standard colours (as provided for the K9 Orbit logo).

*Back of the card*
Include a smaller K9 Orbit logo on the back.

We need the following details for K9 Orbit personnel (as a template for entry):
- Name
- Company Position
- Mobile Number
- Email
- Office Address
- Include the K9 Orbit website: www.k9orbit.com.au

Overall, we'd like to see a design that communicates the adventure of space, professional integrity, and customer service. We look forward to seeing what you can come up with.

Target Market(s)

We provide high quality professional services for the Australian space industry. Our clients include the Southern Launch Bureau and companies working in the space industry.

Contact Information for Business Card

- Name
- Company Position
- Mobile Number
- Email
- Office Address

Requirements
Must have
• See project description.

```html
<!DOCTYPE html>
<html lang="en">
<head>
<meta charset="utf-8">
<title>K9 Orbit — Business Card</title>
<link rel="stylesheet" href="https://fonts.googleapis.com/css2?family=Arimo:wght@400;700&display=swap">
<style>
  :root {
    --page: #d9d9dc;
    --navy: #28286f;
    --brand-violet: #6a6ee0;
    --ink: #333336;
    --rule: #2f6fa8;
    --white: #ffffff;
    --muted: #7c7c86;
    --front-sub: #a9abe6;
  }
  * { box-sizing: border-box; margin: 0; padding: 0; }
  html, body { width: 1200px; height: 874px; overflow: hidden; }
  body {
    background: var(--page);
    position: relative;
    font-family: "Arimo", Arial, sans-serif;
  }
  .card {
    position: absolute;
    left: 300px;
    width: 600px;
    height: 343px;
    overflow: hidden;
    box-shadow: 0 10px 28px rgba(0,0,0,.25);
  }

  /* Front */
  .card-front { top: 52px; background: var(--navy); }
  .orbit-glow {
    position: absolute;
    left: 60px; top: 40px;
    width: 480px; height: 263px;
    border-radius: 50%;
    background: radial-gradient(ellipse at center, rgba(255,255,255,.07) 0%, rgba(255,255,255,.03) 60%, rgba(255,255,255,0) 72%);
  }
  .front-block {
    position: absolute;
    left: 0; right: 0; top: 128px;
    text-align: center;
  }
  .company-name {
    display: inline-flex;
    align-items: center;
    gap: 12px;
    font-family: "Arimo", Arial, sans-serif;
    font-weight: 700;
    font-size: 44px;
    letter-spacing: 0;
    color: var(--brand-violet);
  }
  .company-name .dot {
    width: 16px; height: 16px; border-radius: 50%;
    background: var(--brand-violet);
  }
  .services {
    font-family: "Arimo", Arial, sans-serif;
    font-weight: 400;
  }
  .front-block .services {
    margin-top: 22px;
    font-size: 13px;
    color: var(--front-sub);
  }

  /* Back */
  .card-back { top: 469px; background: var(--white); }
  .name-band {
    position: absolute;
    left: 0; top: 34px;
    width: 300px; height: 82px;
    background: var(--navy);
    padding: 14px 0 0 36px;
    color: var(--white);
  }
  .name-band .person-name {
    font-weight: 700; font-size: 21px; letter-spacing: .5px;
    text-transform: uppercase;
  }
  .name-band .person-role { font-size: 14px; margin-top: 3px; }

  .back-block { position: absolute; right: 40px; top: 124px; text-align: right; }
  .back-block .company-name { font-size: 28px; gap: 8px; color: var(--navy); }
  .back-block .company-name .dot { width: 11px; height: 11px; background: var(--navy); }
  .back-block .services { margin-top: 12px; font-size: 11px; color: var(--muted); }

  .address {
    position: absolute; left: 40px; top: 222px;
    font-style: normal;
    font-size: 15px; line-height: 1.3; color: var(--ink);
  }
  .website {
    position: absolute; left: 40px; top: 272px;
    font-weight: 700; font-size: 15px; color: var(--navy);
    text-decoration: none;
  }
  .contact {
    position: absolute; right: 40px; top: 262px;
    font-size: 15px; line-height: 1.3; color: var(--ink);
  }
  .bottom-rule {
    position: absolute; left: 40px; right: 40px; top: 305px;
    height: 1px; background: var(--rule);
  }
</style>
</head>
<body>
  <section class="card card-front" aria-label="Card front">
    <div class="orbit-glow" role="img" aria-label="Faint orbit decoration"></div>
    <div class="front-block">
      <div class="company-name"><span class="dot"></span>K9 Orbit</div>
      <p class="services">Labour Hire • Consultancy • Project Delivery</p>
    </div>
  </section>

  <section class="card card-back" aria-label="Card back">
    <div class="name-band">
      <p class="person-name">Daniel Hart</p>
      <p class="person-role">President</p>
    </div>
    <div class="back-block">
      <div class="company-name"><span class="dot"></span>K9 Orbit</div>
      <p class="services">Labour Hire • Consultancy • Project Delivery</p>
    </div>
    <address class="address">
      214 Banksia Road<br>Adelaide, SA 5000
    </address>
    <a class="website" href="#">WWW.K9ORBIT.COM.AU</a>
    <div class="contact">
      P. 0412-385-720<br>info@k9orbit.com.au
    </div>
    <div class="bottom-rule"></div>
  </section>
</body>
</html>
```